Software company specialized in data analytics and professional services

We need a landing page design for our business. It should include our logo design. It should have multiple sections :
- stylish head
- what we do (data analytics software, professional services)
- contact form

Target Market(s)

Companies, B2B

Industry/Entity Type

Data

Number of Pages Required

1 page

Font styles to use
Sans Serif

Requirements
Must have
• Dark theme
Should not have
• Gradients on buttons

```html
<!DOCTYPE html>
<html lang="en">
<head>
<meta charset="utf-8">
<title>Quantiva — Data Analysis</title>
<link href="https://fonts.googleapis.com/css2?family=Poppins:wght@600;700;800&family=Montserrat:wght@400;500;600&display=swap" rel="stylesheet">
<style>
:root{
  --bg:#13142b;
  --surface:#1e2042;
  --surface-line:#353868;
  --navy:#0b0c26;
  --magenta:#e0138c;
  --violet:#8d14e3;
  --text:#ffffff;
  --muted:#b4b6cf;
  --soft-pink:#f4cdea;
  --field-text:#6a4060;
  --footer:#0c0d1f;
  --white:#ffffff;
}
*{margin:0;padding:0;box-sizing:border-box}
html,body{width:1200px;height:3956px;overflow:hidden;background:var(--bg)}
body{position:relative;font-family:"Montserrat",sans-serif;color:var(--text)}
.abs{position:absolute}
.display{font-family:"Poppins",sans-serif;font-weight:700}
.dots{display:flex;gap:18px;justify-content:center}
.dots span{width:15px;height:15px;border-radius:50%;background:var(--magenta)}
.dots.light span{background:var(--white)}
.btn{position:absolute;display:flex;align-items:center;justify-content:center;background:var(--magenta);color:var(--white);border-radius:30px;font-size:14px;font-weight:500;letter-spacing:.3px}

/* top bar */
.topbar{left:0;top:0;width:1200px;height:52px;background:linear-gradient(90deg,#08091e,#101249 60%,#1b3f7a);color:var(--white);font-size:14px}
.topbar .item{position:absolute;top:16px;display:flex;align-items:center;gap:10px}
/* nav */
.nav{left:0;top:52px;width:1200px;height:93px;background:var(--bg);border-bottom:1px solid var(--surface-line)}
.brand{position:absolute;left:34px;top:26px;font-family:"Poppins",sans-serif;font-weight:700;font-size:34px;color:var(--magenta);letter-spacing:1px}
.nav .links{position:absolute;left:296px;top:43px;font-size:14px;font-weight:500;color:var(--text)}
.nav .links span{position:absolute;white-space:nowrap}
/* hero */
.hero{left:0;top:145px;width:1200px;height:700px;background:linear-gradient(135deg,#2c2e3a,#55576a 45%,#1f2030)}
.hero-title{left:0;width:1200px;top:280px;text-align:center;color:var(--white);font-size:72px;line-height:84px}
.hero-text{left:0;width:1200px;top:462px;text-align:center;color:var(--white);font-size:17px;line-height:29px}
/* services */
.h2{font-size:46px;text-align:center;width:1200px;left:0;color:var(--text)}
.card{position:absolute;top:995px;width:221px;height:272px;background:var(--surface);border-radius:34px;box-shadow:0 10px 28px rgba(0,0,0,.45)}
.card .band{position:absolute;left:0;top:0;width:221px;height:92px;border-radius:34px 34px 50% 50%/34px 34px 60% 60%;background:linear-gradient(90deg,#e8189a,#b448e8)}
.card .icon{position:absolute;left:62px;top:-8px;width:97px;height:88px;border-radius:0 0 50% 50%;background:var(--surface);display:flex;align-items:center;justify-content:center}
.card h3{position:absolute;top:104px;left:0;width:221px;text-align:center;font-family:"Poppins",sans-serif;font-weight:600;font-size:22px;line-height:23px;color:var(--text)}
.card p{position:absolute;top:160px;left:16px;width:189px;text-align:center;font-size:9px;line-height:13px;color:var(--muted)}
.card .go{position:absolute;left:94px;top:258px;width:33px;height:33px;border-radius:50%;background:#d84bc6;display:flex;align-items:center;justify-content:center}
/* about */
.about-text{left:578px;top:1545px;width:440px;font-size:14px;line-height:24.5px;color:var(--muted)}
/* benefits */
.benefit{position:absolute;left:106px;width:480px}
.benefit .mark{position:absolute;left:0;top:8px;width:56px;height:56px;border-radius:50%;background:var(--white)}
.benefit h4{position:absolute;left:73px;top:0;font-family:"Poppins",sans-serif;font-weight:600;font-size:27px;color:var(--white);white-space:nowrap}
.benefit p{position:absolute;left:79px;top:40px;width:400px;font-size:14px;line-height:24.5px;color:var(--white)}
/* form */
.form{left:636px;top:2702px;width:471px;height:433px;border:1.5px solid var(--surface-line);border-radius:30px;background:var(--surface)}
.field{position:absolute;background:var(--soft-pink);border-radius:20px;font-size:10px;font-weight:600;color:var(--field-text);padding-left:24px;display:flex;align-items:center;letter-spacing:.3px}
/* footer */
.footer{left:0;top:3446px;width:1200px;height:510px;background:var(--footer)}
.quote{left:246px;top:3268px;width:742px;height:245px;background:linear-gradient(90deg,#e0138c,#9b13e0)}
.foot-col{position:absolute;top:3605px;color:var(--white)}
.foot-col h5{font-size:17px;font-weight:600;letter-spacing:.3px}
.foot-col .rule{width:58px;height:3px;background:var(--magenta);margin-top:8px}
.foot-col ul{list-style:none;margin-top:30px}
.foot-col li{font-size:18px;line-height:43.5px}
</style>
</head>
<body>

<header class="abs topbar">
  <div class="item" style="left:822px">
    <svg width="14" height="14" viewBox="0 0 24 24"><path fill="#fff" d="M6.6 10.8a15 15 0 0 0 6.6 6.6l2.2-2.2a1 1 0 0 1 1-.25 11.4 11.4 0 0 0 3.6.57 1 1 0 0 1 1 1V20a1 1 0 0 1-1 1A17 17 0 0 1 3 4a1 1 0 0 1 1-1h3.5a1 1 0 0 1 1 1c0 1.25.2 2.45.57 3.57a1 1 0 0 1-.25 1z"/></svg>
    <span>888 888 8888</span>
  </div>
  <div class="item" style="left:994px">
    <svg width="16" height="12" viewBox="0 0 16 12"><rect width="16" height="12" rx="1.5" fill="#fff"/><path d="M1 1l7 5 7-5" stroke="#101249" stroke-width="1.4" fill="none"/></svg>
    <span>info@domain.com</span>
  </div>
</header>

<nav class="abs nav">
  <div class="brand">QUANTIVA</div>
  <div class="links">
    <span style="left:0">HOME</span>
    <span style="left:109px">ABOUT</span>
    <span style="left:218px">SERVICES</span>
    <span style="left:350px">PROCESS</span>
    <span style="left:484px">TESTIMONIALS</span>
  </div>
  <div class="btn" style="left:977px;top:29px;width:180px;height:40px">GET A QUOTE</div>
</nav>

<section class="abs hero" role="img" aria-label="Photo of a team working on laptops with data dashboards"></section>
<svg class="abs" style="left:0;top:660px" width="1200" height="200" viewBox="0 0 1200 200">
  <defs><linearGradient id="arc" x1="0" x2="1"><stop offset="0" stop-color="#e0138c"/><stop offset="1" stop-color="#9b13e0"/></linearGradient></defs>
  <path d="M0 40 Q600 300 1200 40 L1200 200 L0 200Z" fill="#13142b"/>
  <path d="M0 60 Q600 310 1200 62 L1200 80 Q600 330 0 78Z" fill="url(#arc)"/>
</svg>
<h1 class="abs display hero-title">Best Data<br>Analysis Company</h1>
<p class="abs hero-text">Lorem ipsum dolor sit amet, consectetur adipiscing elit,<br>sed do eiusmod tempor incididunt ut labore<br>et dolore magna aliqua.</p>
<div class="btn" style="left:494px;top:563px;width:180px;height:42px">GET A QUOTE</div>

<h2 class="abs display h2" style="top:882px">What Service We Offer</h2>
<div class="abs dots" style="left:0;width:1200px;top:947px"><span></span><span></span><span></span></div>

<div class="card" style="left:77px">
  <div class="band"></div>
  <div class="icon"><svg width="42" height="42" viewBox="0 0 42 42" fill="none" stroke="#e0138c" stroke-width="1.8"><rect x="6" y="4" width="24" height="30" rx="2"/><circle cx="24" cy="26" r="8"/><path d="M30 32l7 7M11 11h14M11 16h10"/></svg></div>
  <h3>Data<br>Analysis</h3>
  <p>Navigate the complexities of personal tax rebates with ease. Whether you're entitled to a refund due to overpaid taxes, marriage allowance, we're here to guide you through the process.</p>
  <div class="go"><svg width="14" height="14" viewBox="0 0 14 14"><path d="M2 5h5V2l5 5-5 5V9H2z" fill="#fff"/></svg></div>
</div>
<div class="card" style="left:356px">
  <div class="band"></div>
  <div class="icon"><svg width="42" height="42" viewBox="0 0 42 42" fill="none" stroke="#e0138c" stroke-width="1.8"><rect x="9" y="3" width="24" height="36" rx="2"/><circle cx="21" cy="13" r="5"/><path d="M14 34V28M19 34V25M24 34V27M29 34V22"/></svg></div>
  <h3>Reporting<br>Automation</h3>
  <p>If your job requires you to wear a uniform, you could be eligible for a uniform tax rebate. Let us handle the paperwork and help you claim what you deserve.</p>
  <div class="go"><svg width="14" height="14" viewBox="0 0 14 14"><path d="M2 5h5V2l5 5-5 5V9H2z" fill="#fff"/></svg></div>
</div>
<div class="card" style="left:634px">
  <div class="band"></div>
  <div class="icon"><svg width="44" height="42" viewBox="0 0 44 42" fill="none" stroke="#e0138c" stroke-width="1.8"><rect x="4" y="4" width="36" height="26" rx="2"/><rect x="9" y="9" width="7" height="6"/><rect x="19" y="9" width="7" height="6"/><rect x="29" y="9" width="7" height="6"/><circle cx="17" cy="32" r="6"/></svg></div>
  <h3>Data<br>Managment</h3>
  <p>Uncover potential refunds for work-related expenses. From mileage claims to professional subscriptions, we'll identify opportunities to maximize your returns.</p>
  <div class="go"><svg width="14" height="14" viewBox="0 0 14 14"><path d="M2 5h5V2l5 5-5 5V9H2z" fill="#fff"/></svg></div>
</div>
<div class="card" style="left:914px">
  <div class="band"></div>
  <div class="icon"><svg width="42" height="42" viewBox="0 0 42 42" fill="none" stroke="#e0138c" stroke-width="1.8"><rect x="7" y="3" width="22" height="32" rx="2"/><path d="M11 9h12M11 14h8"/><circle cx="28" cy="28" r="9"/><path d="M24 31v-3M28 31v-6M32 31v-4"/></svg></div>
  <h3>Financial<br>Analysis</h3>
  <p>Have you overpaid taxes in the past? Our experts will review your tax history and work to recover any excess payments, ensuring you receive your rightful refund.</p>
  <div class="go"><svg width="14" height="14" viewBox="0 0 14 14"><path d="M2 5h5V2l5 5-5 5V9H2z" fill="#fff"/></svg></div>
</div>

<svg class="abs" style="left:128px;top:1413px" width="374" height="374" viewBox="0 0 374 374">
  <defs><linearGradient id="ring" x1="0" x2="1"><stop offset="0" stop-color="#e0138c"/><stop offset="1" stop-color="#9b13e0"/></linearGradient></defs>
  <circle cx="187" cy="187" r="182" fill="none" stroke="url(#ring)" stroke-width="6"/>
</svg>
<div class="abs" role="img" aria-label="Photo of an office desk with a computer showing a tax return form and a person working on a laptop" style="left:140px;top:1425px;width:350px;height:350px;border-radius:50%;background:linear-gradient(135deg,#c9c4be,#8f877e 55%,#2a2d3a)"></div>

<h2 class="abs display" style="left:580px;top:1440px;font-size:46px;color:var(--text)">About Quantiva</h2>
<div class="abs dots" style="left:581px;top:1511px"><span></span><span></span><span></span></div>
<p class="abs about-text">Lorem ipsum dolor sit amet, consectetur adipiscing elit, sed do eiusmod tempor incididunt ut labore et dolore magna aliqua. Ut enim ad minim veniam, quis nostrud exercitation ullamco laboris nisi ut aliquip ex ea commodo consequat. Duis aute irure dolor in reprehenderit in voluptate velit esse cillum dolore eu fugiat nulla pariatur.</p>
<div class="btn" style="left:578px;top:1715px;width:180px;height:40px">READ MORE</div>

<svg class="abs" style="left:0;top:1880px" width="1200" height="630" viewBox="0 0 1200 630">
  <defs><linearGradient id="bgr" x1="0" x2="1"><stop offset="0" stop-color="#e4138d"/><stop offset="1" stop-color="#9212e3"/></linearGradient></defs>
  <path d="M0 95 Q600 -60 1200 95 L1200 123 Q600 -30 0 123Z" fill="url(#bgr)"/>
  <path d="M0 137 Q600 -12 1200 137 L1200 630 L0 630Z" fill="url(#bgr)"/>
</svg>
<h2 class="abs display h2" style="top:1964px">Program Benefits</h2>
<div class="abs dots light" style="left:0;width:1200px;top:2036px"><span></span><span></span><span></span></div>

<div class="benefit" style="top:2092px;height:120px"><div class="mark"></div><h4>Financial Analytics</h4><p>Lorem ipsum dolor sit amet, consectetur adipiscing elit, sed do eiusmod tempor incididunt ut labore et dolore magna aliqua.</p></div>
<div class="benefit" style="top:2224px;height:120px"><div class="mark"></div><h4>Financial Analytics</h4><p>Lorem ipsum dolor sit amet, consectetur adipiscing elit, sed do eiusmod tempor incididunt ut labore et dolore magna aliqua.</p></div>
<div class="benefit" style="top:2356px;height:120px"><div class="mark"></div><h4>Financial Analytics</h4><p>Lorem ipsum dolor sit amet, consectetur adipiscing elit, sed do eiusmod tempor incididunt ut labore et dolore magna aliqua.</p></div>

<div class="abs" role="img" aria-label="Photo of colleagues smiling together in front of a laptop" style="left:711px;top:2098px;width:374px;height:334px;border-radius:10px;background:linear-gradient(135deg,#6b4a3c,#c98a6a 45%,#e8dcd3)"></div>

<h2 class="abs display h2" style="top:2575px">Contact Us</h2>
<div class="abs dots" style="left:0;width:1200px;top:2639px"><span></span><span></span><span></span></div>

<div class="abs" role="img" aria-label="Street map showing the office location" style="left:88px;top:2714px;width:517px;height:421px;background:linear-gradient(135deg,#3a3d5c,#2a2c46)"></div>

<div class="abs form">
  <div class="field" style="left:33px;top:40px;width:188px;height:40px">NAME</div>
  <div class="field" style="left:234px;top:38px;width:188px;height:40px">PHONE NUMBER</div>
  <div class="field" style="left:33px;top:95px;width:188px;height:40px">EMAIL</div>
  <div class="field" style="left:234px;top:95px;width:188px;height:40px">SUBJECT</div>
  <div class="field" style="left:37px;top:186px;width:389px;height:98px;align-items:flex-start;padding-top:16px;border-radius:14px">MESSAGE</div>
  <div class="btn" style="left:43px;top:310px;width:377px;height:48px;font-size:16px;font-weight:600">SUBMIT DETAILS</div>
</div>

<svg class="abs" style="left:0;top:3320px" width="1200" height="130" viewBox="0 0 1200 130">
  <defs><linearGradient id="fg" x1="0" x2="1"><stop offset="0" stop-color="#e0138c"/><stop offset="1" stop-color="#9b13e0"/></linearGradient></defs>
  <path d="M0 100 Q600 -50 1200 100 L1200 116 Q600 -34 0 116Z" fill="url(#fg)"/>
  <path d="M0 125 Q600 -22 1200 125 L1200 130 L0 130Z" fill="#0c0d1f"/>
</svg>
<div class="abs footer"></div>

<div class="abs quote">
  <div class="abs" role="img" aria-label="Portrait of the client" style="left:92px;top:50px;width:132px;height:132px;border-radius:50%;background:linear-gradient(135deg,#c9cdd6,#4a5265)"></div>
  <div class="abs display" style="left:249px;top:42px;color:#fff;font-size:27px;font-weight:600">Lena Marsh</div>
  <svg class="abs" style="left:249px;top:88px" width="140" height="26" viewBox="0 0 140 26">
    <g fill="#f1c232">
      <path id="st" d="M13 1l3.6 7.6 8.3 1-6.1 5.7 1.6 8.2L13 19.5l-7.4 4 1.6-8.2L1.1 9.6l8.3-1z"/>
      <use href="#st" x="28"/><use href="#st" x="56"/><use href="#st" x="84"/><use href="#st" x="112"/>
    </g>
  </svg>
  <p class="abs" style="left:249px;top:128px;width:330px;color:#fff;font-size:12.5px;line-height:21.5px">Lorem ipsum dolor sit amet, consectetur adipiscing elit, sed do eiusmod tempor incididunt ut labore et dolore magna aliqua. et enim ad minim veniam, quis nostrud</p>
</div>

<div class="foot-col" style="left:323px"><h5>QUICK LINKS</h5><div class="rule"></div>
  <ul style="margin-left:-5px"><li>Home</li><li>About</li><li>Services</li><li>Process</li><li>Contact Us</li></ul></div>
<div class="foot-col" style="left:553px;top:3600px"><h5>OUR SERVICES</h5><div class="rule"></div>
  <ul><li>Home</li><li>About</li><li>Services</li><li>Process</li></ul></div>
<div class="foot-col" style="left:776px"><h5>CONTACT INFO</h5><div class="rule"></div>
  <ul style="margin-top:24px">
    <li style="font-size:15px;display:flex;align-items:center;gap:12px"><svg width="13" height="13" viewBox="0 0 24 24"><path fill="#e0138c" d="M6.6 10.8a15 15 0 0 0 6.6 6.6l2.2-2.2a1 1 0 0 1 1-.25 11.4 11.4 0 0 0 3.6.57 1 1 0 0 1 1 1V20a1 1 0 0 1-1 1A17 17 0 0 1 3 4a1 1 0 0 1 1-1h3.5a1 1 0 0 1 1 1c0 1.25.2 2.45.57 3.57a1 1 0 0 1-.25 1z"/></svg>888 888 8888</li>
    <li style="font-size:15px;display:flex;align-items:center;gap:12px"><svg width="16" height="12" viewBox="0 0 16 12"><rect width="16" height="12" rx="1.5" fill="#e0138c"/><path d="M1 1l7 5 7-5" stroke="#0c0d1f" stroke-width="1.4" fill="none"/></svg>info@domain.com</li>
  </ul></div>

<div class="abs" style="left:311px;top:3898px;width:626px;height:1px;background:#4a4c6a"></div>
<p class="abs" style="left:0;width:1166px;top:3918px;text-align:center;color:#fff;font-size:14.5px">Copyright © 2021. All rights reserved.</p>

</body>
</html>
```